Skin care line needs a LABEL designed!

Fernlight Skin Care... An EARTHY modern boho chic skin care line needs a label designed. It is called Fernlight because there are healing crystals in the product. Holistic, yoga feel, Earthy, feminine.

This contest is for 1 cleanser label- 2 different versions:

Gel Cleanser
Milk Cleanser

Label Size: 4.8125 x 4.8125 in

Winner will be selected to do the labels for:
Toner (5 Versions)
Serum (5 Versions)
Moisturizer (3 Versions)
Sample Label and packaging

Please be prepared to quote a price for the additional labels listed.

Inspiring Brands: **Corvella Studio**, Marigrove Organics, Tessa Wren, Halvenmoor beauty product brands,

Feel free to separate the logo symbol and use it somewhere else in the design.

Target Market(s)

Women ages 30-60

Industry/Entity Type

Skin Care Product

Requirements
Must have
• Tag Line: Inner Peace- Outer Beauty
• Area for ingredients
• Earthy feel
• Large STEP 1 on the front of packaging
• Disclaimer:
• Note: Metaphysical descriptions and healing properties of crystals are not meant to replace medical advice or treat any condition. For external use only.
Nice to have
• www.fernlight-skincare.example
Should not have
• Multiple Colors

```html
<!DOCTYPE html>
<html lang="en">
<head>
<meta charset="utf-8">
<title>Fernlight Skin Care – Gel Cleanser Label</title>
<link rel="stylesheet" href="https://fonts.googleapis.com/css2?family=Poiret+One&display=swap">
<style>
  :root {
    --teal: #74f7e6;
    --teal-soft: #c9fbf4;
    --grey: #8c8c8c;
    --grey-dark: #7a7a7a;
    --white: #ffffff;
  }
  html, body {
    margin: 0;
    padding: 0;
    width: 1200px;
    height: 1200px;
    overflow: hidden;
    background: var(--white);
  }
  .label {
    position: relative;
    width: 1200px;
    height: 1200px;
    background: var(--white);
    font-family: "Poiret One", sans-serif;
    color: var(--grey);
  }
  .band {
    position: absolute;
    left: 0;
    width: 1200px;
    background: var(--teal);
    display: flex;
    align-items: center;
    justify-content: center;
    color: var(--grey-dark);
    -webkit-text-stroke: 2px var(--white);
    paint-order: stroke fill;
  }
  .band--top { top: 0; height: 100px; }
  .band--bottom { bottom: 0; height: 102px; }
  .tagline { font-size: 80px; letter-spacing: 1px; line-height: 1; margin-top: -6px; }
  .step { font-size: 104px; letter-spacing: 2px; line-height: 1; font-weight: 700; }

  .product-name {
    position: absolute;
    left: 55px;
    top: 150px;
    width: 160px;
    height: 900px;
  }

  .brand {
    position: absolute;
    left: 300px;
    top: 190px;
    width: 500px;
    text-align: center;
    color: var(--teal);
    font-size: 78px;
    line-height: 1;
  }
  .brand__sub { display: block; font-size: 54px; margin-top: 8px; }

  .emblem {
    position: absolute;
    left: 395px;
    top: 395px;
    width: 366px;
    height: 366px;
    border-radius: 50%;
    background: radial-gradient(circle, var(--white) 0 22%, var(--teal-soft) 23% 60%, var(--teal) 61% 100%);
  }

  .claim {
    position: absolute;
    left: 300px;
    top: 778px;
    width: 530px;
    text-align: center;
    font-size: 51px;
    line-height: 64px;
    color: var(--grey);
  }

  .info {
    position: absolute;
    left: 821px;
    width: 380px;
    color: var(--grey);
  }
  .info strong { font-weight: 700; color: var(--grey-dark); }
  .directions { top: 152px; font-size: 29px; line-height: 38px; }
  .ingredients { top: 278px; left: 825px; font-size: 29px; }
  .note { top: 655px; left: 830px; font-size: 25px; line-height: 31px; width: 370px; }
  .disclaimer { top: 864px; left: 835px; font-size: 24px; font-weight: 700; }
</style>
</head>
<body>
<div class="label">
  <header class="band band--top">
    <div class="tagline">Inner Peace-Outer Beauty</div>
  </header>

  <svg class="product-name" viewBox="0 0 160 900" aria-label="Gel Cleanser">
    <defs>
      <linearGradient id="nameFill" x1="0" y1="0" x2="1" y2="0">
        <stop offset="0" stop-color="#8c8c8c"/>
        <stop offset="1" stop-color="#74f7e6"/>
      </linearGradient>
    </defs>
    <text transform="translate(142 890) rotate(-90)" x="0" y="0"
          font-family="Poiret One, sans-serif" font-size="190"
          textLength="880" lengthAdjust="spacingAndGlyphs"
          fill="url(#nameFill)">GEL CLEANSER</text>
  </svg>

  <div class="brand">Fernlight<span class="brand__sub">Skin Care</span></div>

  <div class="emblem" role="img" aria-label="Teal lotus mandala emblem"></div>

  <p class="claim" style="margin:0">Our natural<br>oils melt away<br>make-up and impurities</p>

  <div class="info directions"><strong>Directions:</strong> Massage onto<br>skin- rinse.</div>
  <div class="info ingredients"><strong>Ingredients:</strong></div>
  <div class="info note">Note: Metaphysical descriptions and healing properties of crystals are not meant to replace medical advice or treatment any condition. For external use only.</div>
  <div class="info disclaimer">Disclaimer:</div>

  <footer class="band band--bottom">
    <div class="step">Step 1</div>
  </footer>
</div>
</body>
</html>
```